Pagevoより「最前線・空腹がすっと静まる献立&噛み方の手引き」というタイトルの電子書籍を出版予定です。

この本のコンセプトは「食べ物を選んで食べること&その食べ方で食欲が自然におさまること、更にはそれがダイエットと健康維持とアンチエイジングに非常に効果的であること、プラス今流行りのダイエット方(オートファジーダイエット、ミトコンドリア活性化、ケトジェニックダイエット、16時間断食、レクチンフリー 食品の勧め、腸活、SATエクササイズ、オイルの種類など)の説明とご提案(やり方)」をお伝えし、読者の皆様の健康維持に貢献したいということです。

ターゲットは男女ともに考えております。デザインは明るくて「何これ、ダイエットや食品の本にしては発想が新しい!」と興味を持ってもらえることを期待しております。(抽象的ですみません;)

何かご質問・ご提案がありましたらいつでもご連絡ください。
どうぞ宜しくお願いいたします。
*以下2項目の追加記載をお願いいたします。お手数ですがどうぞ宜しくお願いいたします。

・読者プレゼント
星座タイプ別 きみに向く減量術と献立チェック

・著者名: 森川 結奈
皆様、お忙しいところをたくさんのご応募、ありがとうございました!
どれも素敵なデザインでなかなか決めるのが難しいところではありますが、
数日中に決定、上位3名の方にご連絡いたします。

それでは、どうぞしばらくお待ちくださいませ。

取り急ぎ、お礼まで。

Thank you so much!
森川 結奈

当選:miru72_studio様 ー 明るくてフレッシュで清潔感のあるイメージで、何だろう?と書店だったら思わず手に取りたくなる素敵なデザインだと思いました。 次点:ripple_308様 ー デザインが可愛いく親しみやすいのと「食事を抑えるのでなく食欲を抑えるダイエット」など刺さるコピーがとても鋭いと感じました。執筆仲間にも好評でした。 次点: Hnbrook様 ー シンプルで見やすいが故に、逆に何が書いてあるんだろう?と興味を持たせてくれそうなデザインだと感じました。仲間内でも好評でした。

選定が遅くなり大変申し訳ございませんでした。この度は沢山の素敵なデザインをご提案くださり、ありがとうございました。 周りの者と相談の上、悩んだ末に決定させていただきました。 本当に素晴らしい作品ばかりで、デザインをするお仕事の素晴らしさを教えていただきました。 皆様のパワーにインスパイアされ、また二冊目も書きたいと思う原動力をいただきました。 またぜひご縁をいただけたら幸いです。 心より感謝申し上げます。どうもありがとうございました。 皆様のますますのご活躍とご発展をお祈り申し上げます。森川結奈

```html
<!DOCTYPE html>
<html lang="ja">
<head>
<meta charset="utf-8">
<title>最前線・空腹がすっと静まる献立&噛み方の手引き</title>
<link href="https://fonts.googleapis.com/css2?family=Noto+Sans+JP:wght@500;700;900&family=Zen+Maru+Gothic:wght@700;900&display=swap" rel="stylesheet">
<style>
  :root {
    --paper: #ffffff;
    --title-green: #3f8f2f;
    --deep-green: #1f5a26;
    --ribbon-green: #5aa63a;
    --ribbon-dark: #3c7a24;
    --accent-orange: #f08a1c;
    --accent-red: #e2332b;
    --gold: #d9b347;
    --gold-light: #f5dc86;
    --ink: #2a2a2a;
  }
  * { margin: 0; padding: 0; box-sizing: border-box; }
  html, body { width: 750px; height: 1200px; overflow: hidden; background: var(--paper); }
  .cover {
    position: relative; width: 750px; height: 1200px; overflow: hidden;
    background: var(--paper);
    font-family: "Noto Sans JP", sans-serif;
  }
  .food-top {
    position: absolute; left: 0; top: 0; width: 750px; height: 260px;
    background:
      linear-gradient(to bottom, rgba(255,255,255,0) 55%, var(--paper) 100%),
      linear-gradient(100deg, #6f9a3e 0%, #b9463a 22%, #e9c79a 40%, #8a3a2c 55%, #5d8f35 72%, #e48a2e 88%, #6fa347 100%);
  }
  .food-bottom-left {
    position: absolute; left: 0; top: 860px; width: 300px; height: 340px;
    background: radial-gradient(ellipse at 20% 85%, #7aa83f 0%, #c7512e 35%, #e9c347 55%, rgba(255,255,255,0) 75%);
  }
  .food-bottom-right {
    position: absolute; right: 0; top: 1010px; width: 230px; height: 190px;
    background: radial-gradient(ellipse at 85% 90%, #5e8a3a 0%, #d8c9a8 40%, rgba(255,255,255,0) 72%);
  }
  .badge {
    position: absolute; left: 282px; top: 98px; width: 172px; height: 76px;
    border-radius: 10px;
    background: linear-gradient(180deg, var(--gold-light), var(--gold));
    border: 3px solid #fff;
    box-shadow: 0 2px 6px rgba(0,0,0,.25);
    display: flex; align-items: center; justify-content: center;
    font-family: "Noto Sans JP", sans-serif; font-weight: 900; font-size: 46px;
    color: var(--accent-red); letter-spacing: 2px;
  }
  .ribbon { position: absolute; left: 100px; top: 212px; width: 550px; height: 92px; }
  .ribbon-text {
    position: absolute; left: 100px; top: 218px; width: 550px; height: 72px;
    display: flex; align-items: center; justify-content: center;
    font-family: "Zen Maru Gothic", sans-serif; font-weight: 900; font-size: 44px;
    color: #fff; letter-spacing: 3px;
  }
  .title-rule { position: absolute; left: 0; top: 300px; width: 750px; height: 420px; }
  .title {
    position: absolute; left: 0; width: 750px; text-align: center;
    font-family: "Noto Sans JP", sans-serif; font-weight: 900;
    color: var(--title-green);
    -webkit-text-stroke: 10px #fff; paint-order: stroke fill;
    text-shadow: 0 3px 6px rgba(0,0,0,.18);
    line-height: 1;
  }
  .title-line1 { top: 318px; font-size: 140px; letter-spacing: 4px; }
  .title-amp { top: 420px; font-size: 84px; color: var(--accent-orange); z-index: 2; }
  .title-line2 { top: 468px; font-size: 140px; letter-spacing: 4px; }
  .title-tail { top: 618px; font-size: 80px; color: var(--deep-green); letter-spacing: 4px; }
  .author {
    position: absolute; left: 0; top: 722px; width: 750px; text-align: center;
    font-family: "Noto Sans JP", sans-serif; font-weight: 700; font-size: 40px;
    color: var(--ink); letter-spacing: 6px;
  }
  .notepad {
    position: absolute; left: 325px; top: 850px; width: 215px; height: 280px;
    background: linear-gradient(180deg, #ffffff, #f1f1ee);
    border: 2px solid #d8d8d2; border-radius: 6px;
    transform: rotate(-4deg);
    box-shadow: 0 4px 10px rgba(0,0,0,.15);
  }
  .diag-left {
    position: absolute; left: 18px; top: 830px; transform: rotate(-22deg); transform-origin: left top;
    font-family: "Zen Maru Gothic", sans-serif; font-weight: 900; line-height: 1.1;
    -webkit-text-stroke: 8px #fff; paint-order: stroke fill;
  }
  .diag-left .line-a { display: block; font-size: 44px; color: var(--accent-orange); padding-left: 20px; }
  .diag-left .line-b { display: block; font-size: 50px; color: var(--title-green); }
  .diag-right {
    position: absolute; left: 520px; top: 760px; transform: rotate(56deg); transform-origin: left top;
    font-family: "Noto Sans JP", sans-serif; font-weight: 900; line-height: 1.15;
    -webkit-text-stroke: 8px #fff; paint-order: stroke fill; white-space: nowrap;
  }
  .diag-right .gift { display: block; font-size: 46px; color: var(--accent-red); }
  .diag-right .type { display: block; font-size: 38px; color: var(--ink); padding-left: 30px; }
</style>
</head>
<body>
<main class="cover">
  <div class="food-top" role="img" aria-label="肉・魚・野菜・果物・ナッツなど色とりどりの食材の写真"></div>
  <div class="food-bottom-left" role="img" aria-label="トマトやアボカド、レモン、葉野菜の写真"></div>
  <div class="food-bottom-right" role="img" aria-label="シード類やヘルシーな食材の写真"></div>

  <div class="badge">最前線</div>

  <svg class="ribbon" viewBox="0 0 550 92" aria-hidden="true">
    <polygon points="0,20 40,20 40,88 0,88 18,54" fill="var(--ribbon-dark)"/>
    <polygon points="550,20 510,20 510,88 550,88 532,54" fill="var(--ribbon-dark)"/>
    <rect x="30" y="6" width="490" height="72" fill="var(--ribbon-green)"/>
  </svg>
  <div class="ribbon-text">空腹がすっと静まる</div>

  <svg class="title-rule" viewBox="0 0 750 420" aria-hidden="true">
    <line x1="40" y1="40" x2="80" y2="150" stroke="var(--gold)" stroke-width="3"/>
    <line x1="60" y1="30" x2="100" y2="140" stroke="var(--gold)" stroke-width="3"/>
    <line x1="710" y1="40" x2="670" y2="150" stroke="var(--gold)" stroke-width="3"/>
    <line x1="690" y1="30" x2="650" y2="140" stroke="var(--gold)" stroke-width="3"/>
  </svg>

  <h1>
    <span class="title title-line1">献立</span>
    <span class="title title-amp">&amp;</span>
    <span class="title title-line2">噛み方</span>
    <span class="title title-tail">の手引き</span>
  </h1>

  <p class="author">森川 結奈</p>

  <div class="notepad" role="img" aria-label="手書きのメモが書かれたメモ帳とペンのイラスト"></div>

  <p class="diag-left"><span class="line-a">減量術と</span><span class="line-b">献立チェック</span></p>
  <p class="diag-right"><span class="gift">読者プレゼント</span><span class="type">星座タイプ別</span></p>
</main>
</body>
</html>
```